Take my logo and make me some cool looking business cards

I've got a logo that we've trademarked so you can't change the logo but you can change it's color combo and find a fun way to incorporate it into a new business card design that is fresh, stylish, and can be applied to some cool medium cost materials (plastic, wood, metal, etc). Basically, we're looking for business cards that stand out in a good way.
Here's the logo we're currently using:
Thanks to everyone that has submitted designs. We've narrowed down to the top 4 designs and tried to eliminate old versions or designs that just didn't match our vision as quickly as we could. We don't plan on keeping this open for the full 9 days; we plan on selecting a design in the next 48 hours; with the goal of having something in the hands of a printer, preferably plastic printer, by Thursday AM Pacific Time.
Business
- must include our existing logo

```html
<!DOCTYPE html>
<html lang="en">
<head>
<meta charset="utf-8">
<title>Tidewell Business Card – Front and Back</title>
<link rel="stylesheet" href="https://fonts.googleapis.com/css2?family=Figtree:wght@400;600;700&family=Open+Sans:wght@400&display=swap">
<style>
  :root {
    --sheet-bg: #d1d2d4;
    --badge-bg: #7c7d80;
    --label-ink: #5a5b5e;
    --card-white: #ffffff;
    --card-blue: #0a6db4;
    --ink: #111111;
    --emboss-light: #f1f1f1;
    --emboss-blue: #0966ab;
    --logo-white: #ffffff;
  }
  * { box-sizing: border-box; margin: 0; padding: 0; }
  html, body {
    width: 1091px;
    height: 1200px;
    overflow: hidden;
    background: var(--sheet-bg);
  }
  .sheet {
    position: relative;
    width: 1091px;
    height: 1200px;
    background: var(--sheet-bg);
    font-family: "Open Sans", sans-serif;
  }
  .step-badge {
    position: absolute;
    left: 48px;
    top: 48px;
    width: 74px;
    height: 74px;
    border-radius: 50%;
    background: var(--badge-bg);
    color: #ffffff;
    font-family: "Open Sans", sans-serif;
    font-weight: 400;
    font-size: 44px;
    line-height: 74px;
    text-align: center;
  }
  .side-label {
    position: absolute;
    left: 202px;
    width: 687px;
    text-align: center;
    color: var(--label-ink);
    font-size: 32px;
    line-height: 1;
  }
  .side-label--front { top: 38px; }
  .side-label--back { top: 627px; }
  .card {
    position: absolute;
    left: 202px;
    width: 687px;
    height: 393px;
    overflow: hidden;
  }
  .card--front { top: 93px; background: var(--card-white); }
  .card--back { top: 682px; background: var(--card-blue); }
  .wordmark {
    position: absolute;
    left: 0;
    width: 100%;
    text-align: center;
    font-family: "Figtree", sans-serif;
    font-weight: 600;
    font-size: 96px;
    letter-spacing: 6px;
    line-height: 1;
  }
  .wordmark--emboss-front { top: 70px; color: var(--emboss-light); }
  .wordmark--emboss-back { top: 63px; color: var(--emboss-blue); transform: scaleX(-1); }
  .wordmark--main { top: 207px; color: var(--logo-white); }
  .contact {
    position: absolute;
    left: 0;
    top: 196px;
    width: 100%;
    text-align: center;
    font-family: "Figtree", sans-serif;
    color: var(--ink);
  }
  .contact__name { font-weight: 700; font-size: 27px; line-height: 34px; }
  .contact__role { font-weight: 400; font-size: 22px; line-height: 28px; margin-bottom: 14px; }
  .contact__line { font-weight: 400; font-size: 19.5px; line-height: 26px; }
  .card-note {
    position: absolute;
    left: 202px;
    top: 503px;
    color: var(--label-ink);
    font-size: 23px;
    line-height: 1.2;
  }
</style>
</head>
<body>
  <main class="sheet">
    <div class="step-badge">1</div>

    <h2 class="side-label side-label--front">Front Side</h2>
    <section class="card card--front" aria-label="Card front">
      <div class="wordmark wordmark--emboss-front" aria-hidden="true">TIDEWELL</div>
      <div class="contact">
        <p class="contact__name">Jordan Hale</p>
        <p class="contact__role">CEO</p>
        <p class="contact__line">418 Marlow Avenue</p>
        <p class="contact__line">Cedar Point, CA 94120</p>
        <p class="contact__line">+140 8555 0192</p>
      </div>
    </section>
    <p class="card-note">Desc: embossed logo.</p>

    <h2 class="side-label side-label--back">Back Side</h2>
    <section class="card card--back" aria-label="Card back">
      <div class="wordmark wordmark--emboss-back" aria-hidden="true">TIDEWELL</div>
      <div class="wordmark wordmark--main">TIDEWELL</div>
    </section>
  </main>
</body>
</html>
```